Boutique Barre Studio in Geneva

Business card for pilates and dance studio. We are a brand new studio and love our fresh image with our yellow color. This business card is meant for our founder.

```html
<!DOCTYPE html>
<html lang="en">
<head>
<meta charset="utf-8">
<title>Velour Barre – Business Card</title>
<link rel="stylesheet" href="https://fonts.googleapis.com/css2?family=Oswald:wght@500&family=Poppins:wght@400;500&display=swap">
<style>
  :root {
    --backdrop: #2b2b2d;
    --card: #1c1c1e;
    --card-back-light: #5a5a5c;
    --card-back-dark: #0b0b0c;
    --accent: #f2e27a;
    --ink-light: #f4f4f4;
    --rule: #6d6d6d;
  }
  * { margin: 0; padding: 0; box-sizing: border-box; }
  html, body { width: 1200px; height: 1108px; overflow: hidden; }
  body {
    background: var(--backdrop);
    position: relative;
    font-family: "Poppins", sans-serif;
  }
  .card {
    position: absolute;
    top: 234px;
    width: 400px;
    height: 640px;
    border-radius: 22px;
    overflow: hidden;
  }
  .card--front { left: 150px; background: var(--card); text-align: center; }
  .card--back { left: 650px; }

  .brand-name {
    position: absolute;
    top: 120px; left: 0; right: 0;
    font-family: "Poppins", sans-serif;
    font-weight: 500;
    font-size: 52px;
    line-height: 1.1;
    color: var(--accent);
  }
  .person-name {
    position: absolute;
    top: 330px; left: 0; right: 0;
    font-family: "Oswald", sans-serif;
    font-weight: 500;
    font-size: 38px;
    color: var(--accent);
    line-height: 1;
  }
  .person-role {
    position: absolute;
    top: 376px; left: 0; right: 0;
    font-size: 17px;
    color: var(--ink-light);
  }
  .contact-icons {
    position: absolute;
    top: 416px; left: 40px; right: 40px;
    display: flex; align-items: center; gap: 10px;
  }
  .contact-icons .rule { flex: 1; height: 1px; background: var(--rule); }
  .icon {
    width: 30px; height: 30px;
    background: var(--accent);
    border-radius: 4px;
    display: flex; align-items: center; justify-content: center;
  }
  .contact-list {
    position: absolute;
    top: 460px; left: 0; right: 0;
    list-style: none;
    font-size: 17px;
    line-height: 27px;
    color: var(--ink-light);
  }
  .divider {
    position: absolute;
    top: 554px; left: 70px; right: 70px;
    height: 1px; background: var(--rule);
  }
  .address {
    position: absolute;
    top: 566px; left: 0; right: 0;
    font-style: normal;
    font-size: 17px;
    line-height: 26px;
    color: var(--ink-light);
  }

  .back-pattern {
    position: absolute; inset: 0;
    background: linear-gradient(210deg, var(--card-back-light) 0%, #2a2a2c 45%, var(--card-back-dark) 100%);
  }
  .back-mark {
    position: absolute;
    left: 0; right: 0; top: 440px;
    display: flex; flex-direction: column; align-items: center; gap: 8px;
  }
  .back-mark .dot {
    width: 46px; height: 46px; border-radius: 50%;
    background: var(--accent);
  }
  .back-mark .label {
    font-family: "Poppins", sans-serif;
    font-weight: 500;
    font-size: 14px;
    color: var(--accent);
  }
</style>
</head>
<body>
  <section class="card card--front" aria-label="Business card front">
    <h1 class="brand-name">Velour<br>Barre</h1>
    <h2 class="person-name">Amélie Fontaine</h2>
    <p class="person-role">Managing Director</p>
    <div class="contact-icons">
      <span class="rule"></span>
      <span class="icon" aria-label="Phone">
        <svg width="18" height="18" viewBox="0 0 24 24"><path fill="#1c1c1e" d="M6.6 10.8a15.5 15.5 0 0 0 6.6 6.6l2.2-2.2c.3-.3.7-.4 1-.2 1.1.4 2.3.6 3.6.6.6 0 1 .4 1 1V20c0 .6-.4 1-1 1C10.6 21 3 13.4 3 4c0-.6.4-1 1-1h3.5c.6 0 1 .4 1 1 0 1.3.2 2.5.6 3.6.1.3 0 .7-.2 1z"/></svg>
      </span>
      <span class="icon" aria-label="Email">
        <svg width="18" height="18" viewBox="0 0 24 24"><rect x="3" y="6" width="18" height="12" fill="none" stroke="#1c1c1e" stroke-width="2"/><path d="M3 6l9 7 9-7" fill="none" stroke="#1c1c1e" stroke-width="2"/></svg>
      </span>
      <span class="icon" aria-label="Website">
        <svg width="18" height="18" viewBox="0 0 24 24"><circle cx="12" cy="12" r="9" fill="none" stroke="#1c1c1e" stroke-width="2"/><path d="M3 12h18M12 3c3 3 3 15 0 18M12 3c-3 3-3 15 0 18" fill="none" stroke="#1c1c1e" stroke-width="1.6"/></svg>
      </span>
      <span class="rule"></span>
    </div>
    <ul class="contact-list">
      <li>022-310 48 57</li>
      <li>hello@velourbarre.ch</li>
      <li>www.velourbarre.ch</li>
    </ul>
    <div class="divider"></div>
    <address class="address">18, Rue du Rhône<br>1204, Geneva</address>
  </section>

  <section class="card card--back" aria-label="Business card back">
    <div class="back-pattern" role="img" aria-label="Repeating glossy emblem pattern on black, fading from grey at top right to black at bottom left"></div>
    <div class="back-mark">
      <span class="dot"></span>
      <span class="label">Velour Barre</span>
    </div>
  </section>
</body>
</html>
```